Lien Post Card - (5.5 x 8.5)

FRONT OF POSTCARD
Is a Property Lien Putting Your Home at Risk?
HOA Liens • Tax Liens • Municipal Charges • Other Property-Related Liens
You may have options to resolve outstanding liens and protect your home.
A Refinance or Home Equity Line of Credit (HELOC) may help you:
✔ Pay off qualifying liens
✔ Consolidate debt into one manageable payment
✔ Access your home's equity
✔ Improve your financial flexibility
✔ Avoid additional penalties, fees, or collection actions
Don't wait until the situation becomes more difficult.
Call today for a confidential review of your options.
Bluegate Lending Partners, Inc.
(800) 647-2915 x 42
www.bluegatelendco.com
NMLS #381640
BACK OF POSTCARD
Your Home Equity Could Be the Solution
If you have received notices regarding:
• Delinquent Property Taxes
• HOA or Condo Association Assessments
• Municipal Utility Liens
• Special Assessments
• Other Property-Related Obligations
You may qualify for financing options designed to help satisfy those obligations and bring your property current.
Our experienced mortgage professionals can review your situation and discuss available programs, including:
• Cash-Out Refinancing
• Home Equity Lines of Credit (HELOCs)
• Home Equity Loans
• Debt Consolidation Solutions
Free Consultation • No Obligation
Contact Marcus Delaney today at (800) 647-2915 x42 or mdelaney@bluegatelendco.com (NMLS #57308)

```html
<!DOCTYPE html>
<html lang="en">
<head>
<meta charset="utf-8">
<title>Lien Postcard – Bluegate Lending Partners</title>
<link rel="stylesheet" href="https://fonts.googleapis.com/css2?family=Montserrat:wght@500;600;700;800&family=Poppins:wght@500;600;700;800&family=Oswald:wght@500&display=swap">
<style>
  :root{
    --navy:#1a2f80;
    --navy-deep:#0c1a52;
    --ink:#10142e;
    --gold:#d9a441;
    --gold-light:#f3c46b;
    --gold-deep:#a9782e;
    --red:#c3141b;
    --white:#ffffff;
    --paper:#ffffff;
    --muted:#cfcfcf;
  }
  *{box-sizing:border-box;margin:0;padding:0}
  html,body{width:1200px;height:1200px;overflow:hidden;background:var(--paper)}
  body{position:relative;font-family:"Poppins",sans-serif}
  .card{position:absolute;left:198px;width:804px;height:520px;background:var(--white);overflow:hidden;box-shadow:0 6px 22px rgba(0,0,0,.18)}
  .card--front{top:62px}
  .card--back{top:629px;height:521px}
  .abs{position:absolute}
  svg.icon{display:block}

  /* FRONT */
  .hero{left:0;top:0;width:420px;height:387px;clip-path:polygon(0 0,420px 0,396px 387px,0 387px);
    background:linear-gradient(160deg,#1d2f86 0%,#16287a 45%,#0d1b5c 100%)}
  .benefit-panel{left:396px;top:0;width:408px;height:387px;clip-path:polygon(24px 0,408px 0,408px 387px,0 387px);
    background:linear-gradient(160deg,#b4802f 0%,#d9a441 45%,#f5c46c 100%)}
  .divider{left:0;top:0}
  .headline{left:35px;top:28px;color:var(--white);font-family:"Montserrat",sans-serif;font-weight:500;font-size:28px;line-height:32px;letter-spacing:-.2px}
  .headline .gold{display:block;background:linear-gradient(180deg,var(--gold-light),var(--gold));-webkit-background-clip:text;background-clip:text;color:transparent}
  .headline .home{font-size:58px;line-height:54px;margin-top:4px}
  .headline .risk{font-size:96px;line-height:80px;letter-spacing:-2px}
  .lien{display:flex;align-items:center;gap:7px;color:var(--white);font-size:14px;font-weight:500;line-height:16px}
  .ring{width:31px;height:31px;border-radius:50%;background:var(--white);border:3px solid var(--gold);display:flex;align-items:center;justify-content:center;flex:none}
  .ring svg{width:14px;height:14px}
  .hero-note{left:39px;top:341px;color:var(--white);font-family:"Montserrat",sans-serif;font-weight:500;font-size:12.5px;line-height:16px}
  .offer-title{left:448px;top:28px;font-family:"Poppins",sans-serif;font-weight:600;font-size:24px;line-height:29px;color:var(--ink)}
  .offer-title .light{color:var(--white)}
  .benefit{display:flex;align-items:center;gap:9px;font-size:10.5px;line-height:12.5px;font-weight:600;color:var(--ink)}
  .badge{width:28px;height:28px;border-radius:50%;background:var(--navy);border:2px solid var(--gold-light);display:flex;align-items:center;justify-content:center;flex:none;box-shadow:0 1px 3px rgba(0,0,0,.3)}
  .badge svg{width:13px;height:13px}
  .urgent{left:398px;top:290px;width:200px;height:97px;background:var(--red);clip-path:polygon(6px 0,200px 0,200px 97px,0 97px)}
  .urgent p{position:absolute;left:29px;top:17px;color:var(--white);font-weight:800;font-style:italic;font-size:17.5px;line-height:18px}
  .urgent p .caps{text-transform:uppercase}
  .couple-photo{left:584px;top:208px;width:220px;height:179px;background:linear-gradient(135deg,#d8a752 0%,#5e5650 45%,#2f3a57 100%);clip-path:polygon(30px 40px,110px 0,220px 0,220px 179px,0 179px)}
  .brand{display:flex;align-items:center;gap:8px;color:var(--navy);font-family:"Poppins",sans-serif;font-weight:700;font-size:16px;line-height:19px}
  .brand .dot{width:26px;height:26px;border-radius:50%;background:var(--gold);flex:none}
  .brand--front{left:34px;top:426px;width:160px}
  .cta{left:219px;top:420px;width:558px;height:31px;border-radius:16px;background:var(--navy);overflow:hidden;display:flex;align-items:center}
  .cta .call{width:128px;height:100%;background:var(--red);border-radius:16px;border:2px solid var(--navy);color:var(--white);font-weight:700;font-size:16px;display:flex;align-items:center;justify-content:center}
  .cta .review{color:var(--white);font-weight:600;font-size:16px;margin-left:12px;letter-spacing:.1px}
  .contact-row{top:466px;display:flex;align-items:center;gap:6px;color:var(--ink);font-size:15px;font-weight:500}
  .contact-row .ico{width:18px;height:18px;border-radius:50%;background:var(--navy);display:flex;align-items:center;justify-content:center}
  .contact-row .ico svg{width:10px;height:10px}
  .nmls-front{left:650px;top:466px;color:var(--navy);font-weight:700;font-size:15px}

  /* BACK */
  .city{left:0;top:0;width:238px;height:431px;background:linear-gradient(180deg,#0d1533 0%,#151c33 55%,#05070f 100%)}
  .back-title{left:32px;top:21px;color:var(--white);font-family:"Montserrat",sans-serif;font-weight:600;font-size:24px;line-height:21.5px}
  .back-title .gold{color:var(--gold)}
  .notice-lead{left:32px;top:119px;color:var(--gold);font-weight:600;font-size:9.7px}
  .notice{display:flex;align-items:center;gap:10px;color:var(--white);font-size:9.3px;font-weight:600;line-height:11px;left:36px}
  .notice .ring{width:27px;height:27px;border-width:3px}
  .notice .ring svg{width:12px;height:12px}
  .qualify{left:32px;top:346px;width:175px;font-size:9.4px;line-height:13.3px;font-weight:600;color:var(--gold)}
  .qualify .white{color:var(--white)}
  .assure-band{left:0;top:431px;width:240px;height:90px;background:linear-gradient(90deg,#1b3180,#213a93)}
  .assure{left:32px;display:flex;align-items:center;gap:5px;color:var(--white);font-family:"Oswald",sans-serif;font-weight:500;font-size:13.5px;letter-spacing:-.2px}
  .assure .tick{width:12px;height:12px;border-radius:50%;background:var(--gold);display:flex;align-items:center;justify-content:center}
  .assure .tick svg{width:8px;height:8px}
  .advisor-photo{left:158px;top:315px;width:130px;height:206px;background:linear-gradient(180deg,#1d1d22 0%,#3a3a44 40%,#141418 100%);clip-path:polygon(52px 0,108px 0,116px 30px,130px 60px,130px 206px,12px 206px,0 120px,30px 60px)}
  .programs-title{left:259px;top:21px;font-family:"Montserrat",sans-serif;font-weight:700;font-size:15.5px;line-height:16.8px;color:var(--navy)}
  .programs-title .gold{color:var(--gold-deep)}
  .pill{left:238px;width:182px;height:41px;border-radius:0 14px 14px 0;display:flex;align-items:center;color:var(--white);font-family:"Montserrat",sans-serif;font-weight:600;font-size:12px;line-height:10.8px;text-transform:uppercase;box-shadow:0 1px 3px rgba(0,0,0,.25)}
  .pill--gold{background:linear-gradient(180deg,#c99a45,#a9782e)}
  .pill--navy{background:linear-gradient(180deg,#223a95,#1a2f80)}
  .pill .check{width:20px;height:20px;border-radius:50%;background:var(--white);margin:0 10px 0 23px;flex:none;display:flex;align-items:center;justify-content:center}
  .pill .check svg{width:11px;height:11px}
  .contact-label{left:293px;top:357px;color:var(--gold-deep);font-family:"Montserrat",sans-serif;font-weight:500;font-size:12px;letter-spacing:2.6px}
  .advisor-name{left:296px;top:374px;color:var(--navy);font-family:"Montserrat",sans-serif;font-weight:700;font-size:26px;line-height:26px}
  .advisor-line{left:306px;display:flex;align-items:center;gap:8px;font-size:8.8px;font-weight:500;color:var(--ink)}
  .advisor-line .ico{width:12px;height:12px;border-radius:50%;background:var(--gold);display:flex;align-items:center;justify-content:center}
  .advisor-line .ico svg{width:7px;height:7px}
  .advisor-nmls{left:306px;top:481px;color:var(--navy);font-weight:700;font-size:10px}
  .brand--back{left:518px;top:46px;width:150px;font-size:14px;line-height:17px}
  .stamp{left:692px;top:27px;width:67px;height:67px;background:var(--muted)}
</style>
</head>
<body>
<svg width="0" height="0" style="position:absolute">
  <defs>
    <symbol id="i-home" viewBox="0 0 16 16"><path d="M8 1.5 1 7.5h2v7h4v-4h2v4h4v-7h2z" fill="currentColor"/></symbol>
    <symbol id="i-tick" viewBox="0 0 16 16"><path d="M2.5 8.5 6.5 12.5 13.5 4" fill="none" stroke="currentColor" stroke-width="2.6" stroke-linecap="round" stroke-linejoin="round"/></symbol>
    <symbol id="i-phone" viewBox="0 0 16 16"><path d="M4.2 1.5 6.6 4 5.3 6.1c.9 1.8 2.3 3.2 4.1 4.1l2.1-1.3 2.5 2.4-1.6 2.6C6.7 13.6 2.4 9.3 1.6 3.1z" fill="currentColor"/></symbol>
    <symbol id="i-mail" viewBox="0 0 16 16"><rect x="1.5" y="3.5" width="13" height="9" rx="1" fill="none" stroke="currentColor" stroke-width="1.6"/><path d="M2 4.5 8 9l6-4.5" fill="none" stroke="currentColor" stroke-width="1.6"/></symbol>
  </defs>
</svg>

<!-- FRONT -->
<section class="card card--front">
  <div class="abs hero" role="img" aria-label="Photo of a two-storey house at dusk tinted deep blue"></div>
  <div class="abs benefit-panel"></div>
  <svg class="abs divider" width="804" height="387"><line x1="418" y1="0" x2="394" y2="387" stroke="#fff" stroke-width="2"/></svg>

  <h1 class="abs headline">IS A PROPERTY LIEN<br>PUTTING YOUR<span class="gold home">HOME AT</span><span class="gold risk">RISK?</span></h1>

  <div class="abs lien" style="left:36px;top:246px"><span class="ring"><svg class="icon" style="color:var(--navy)"><use href="#i-home"/></svg></span>HOA Liens</div>
  <div class="abs lien" style="left:166px;top:244px"><span class="ring"><svg class="icon" style="color:var(--navy)"><use href="#i-home"/></svg></span>Municipal Charges</div>
  <div class="abs lien" style="left:36px;top:289px"><span class="ring"><svg class="icon" style="color:var(--navy)"><use href="#i-home"/></svg></span>Tax Liens</div>
  <div class="abs lien" style="left:164px;top:282px"><span class="ring"><svg class="icon" style="color:var(--navy)"><use href="#i-home"/></svg></span>Other Property<br>Related Liens</div>

  <p class="abs hero-note">YOU MAY HAVE OPTIONS TO RESOLVE<br>OUTSTANDING LIENS AND&nbsp; PROTECT YOUR HOME.</p>

  <h2 class="abs offer-title">A Refinance or<br><span class="light">Home Equity Line of Credit</span><br>(HELOC) may help you:</h2>

  <div class="abs benefit" style="left:445px;top:129px"><span class="badge"><svg class="icon" style="color:#fff"><use href="#i-tick"/></svg></span>Pay off<br>qualifying liens</div>
  <div class="abs benefit" style="left:590px;top:129px"><span class="badge"><svg class="icon" style="color:#fff"><use href="#i-tick"/></svg></span>Improve your<br>financial flexibility</div>
  <div class="abs benefit" style="left:445px;top:175px"><span class="badge"><svg class="icon" style="color:#fff"><use href="#i-home"/></svg></span>Access your<br>home's equity</div>
  <div class="abs benefit" style="left:590px;top:175px"><span class="badge"><svg class="icon" style="color:#fff"><use href="#i-tick"/></svg></span>Avoid additional penalties,<br>fees, or collection actions</div>
  <div class="abs benefit" style="left:445px;top:225px"><span class="badge"><svg class="icon" style="color:#fff"><use href="#i-tick"/></svg></span>Consolidate<br>debt into one<br>manageable<br>payment</div>

  <div class="abs urgent"><p>Don't wait until<br><span class="caps">the situation<br>becomes</span><br>more difficult.</p></div>
  <div class="abs couple-photo" role="img" aria-label="Photo of a worried couple at a table reviewing bills on a laptop"></div>

  <div class="abs brand brand--front"><span class="dot"></span>Bluegate Lending Partners</div>

  <div class="abs cta"><span class="call">CALL TODAY</span><span class="review">FOR A CONFIDENTIAL REVIEW OF YOUR OPTIONS</span></div>
  <div class="abs contact-row" style="left:230px"><span class="ico"><svg class="icon" style="color:#fff"><use href="#i-phone"/></svg></span>(800) 647-2915 x 42</div>
  <div class="abs contact-row" style="left:422px"><span class="ico"><svg class="icon" style="color:#fff"><use href="#i-mail"/></svg></span>www.bluegatelendco.com</div>
  <div class="abs nmls-front">NMLS #381640</div>
</section>

<!-- BACK -->
<section class="card card--back">
  <div class="abs city" role="img" aria-label="Photo of a city skyline at night in dark blue tones"></div>
  <h2 class="abs back-title">YOUR<br><span class="gold">HOME EQUITY</span><br>COULD BE THE<br>SOLUTION</h2>
  <p class="abs notice-lead">If you have received notices regarding</p>

  <div class="abs notice" style="top:145px"><span class="ring"><svg class="icon" style="color:var(--navy)"><use href="#i-home"/></svg></span>Delinquent<br>Property Taxes</div>
  <div class="abs notice" style="top:179px"><span class="ring"><svg class="icon" style="color:var(--navy)"><use href="#i-home"/></svg></span>HOA or Condo<br>Association<br>Assessments</div>
  <div class="abs notice" style="top:225px"><span class="ring"><svg class="icon" style="color:var(--navy)"><use href="#i-home"/></svg></span>Municipal<br>Utility Liens</div>
  <div class="abs notice" style="top:262px"><span class="ring"><svg class="icon" style="color:var(--navy)"><use href="#i-home"/></svg></span>Special<br>Assessments</div>
  <div class="abs notice" style="top:299px"><span class="ring"><svg class="icon" style="color:var(--navy)"><use href="#i-home"/></svg></span>Other Property<br>Related Obligations</div>

  <p class="abs qualify">You may qualify for financing options designed to help satisfy those obligations and <span class="white">bring your property current.</span></p>

  <div class="abs assure-band"></div>
  <div class="abs advisor-photo" role="img" aria-label="Photo of the loan officer in a dark coat and hat"></div>
  <div class="abs assure" style="top:447px"><span class="tick"><svg class="icon" style="color:#fff"><use href="#i-tick"/></svg></span>FREE CONSULTATION</div>
  <div class="abs assure" style="top:469px"><span class="tick"><svg class="icon" style="color:#fff"><use href="#i-tick"/></svg></span>NO OBLIGATION</div>

  <svg class="abs" style="left:0;top:0" width="804" height="521"><path d="M482 0 C430 170 430 350 482 521" fill="none" stroke="#e3e3e3" stroke-width="3"/></svg>

  <h3 class="abs programs-title">OUR EXPERIENCED<br>MORTGAGE<br>PROFESSIONALS<br><span class="gold">CAN REVIEW YOUR<br>SITUATION &amp; DISCUSS<br>AVAILABLE PROGRAMS,<br>INCLUDING:</span></h3>

  <div class="abs pill pill--gold" style="top:146px"><span class="check"><svg class="icon" style="color:var(--gold-deep)"><use href="#i-tick"/></svg></span>Cash-Out<br>Refinancing</div>
  <div class="abs pill pill--navy" style="top:189px"><span class="check"><svg class="icon" style="color:var(--navy)"><use href="#i-tick"/></svg></span>Home Equity<br>Lines of<br>Credit (HELOCs)</div>
  <div class="abs pill pill--gold" style="top:234px"><span class="check"><svg class="icon" style="color:var(--gold-deep)"><use href="#i-tick"/></svg></span>Home<br>Equity Loans</div>
  <div class="abs pill pill--navy" style="top:281px"><span class="check"><svg class="icon" style="color:var(--navy)"><use href="#i-tick"/></svg></span>Debt<br>Consolidation<br>Solutions</div>

  <p class="abs contact-label">CONTACT</p>
  <p class="abs advisor-name">MARCUS<br>DELANEY</p>
  <div class="abs advisor-line" style="top:441px"><span class="ico"><svg class="icon" style="color:#fff"><use href="#i-phone"/></svg></span>(800) 647-2915 x42</div>
  <div class="abs advisor-line" style="top:458px"><span class="ico"><svg class="icon" style="color:#fff"><use href="#i-mail"/></svg></span>mdelaney@bluegatelendco.com</div>
  <p class="abs advisor-nmls">NMLS #381640</p>

  <div class="abs brand brand--back"><span class="dot"></span>Bluegate Lending Partners</div>
  <div class="abs stamp"></div>
</section>
</body>
</html>
```